Silver Lantern Golf Club is a golf community dedicated to building productive relationships beginning with the unifying foundation of the great game.
Membership in the Silver Lantern Golf Club is simple, ask to join. The Membership Committee accepts a prospective member request upon confirmation of support for the club’s purpose.
The Silver Lantern Golf Club has only two rules:
1.) Create productive relationships building around an initial common thread
2.) When tempted to cut the last relationship thread, remember rule #1
Silver Lantern Golf Club members receive invitations to occasional club events but are also encouraged to create smaller events hosted by individual members. Members are not required to brand gatherings as official Silver Lantern Golf Club events. We believe when two or more of our members are together, the world gets better.
What are the dues? Members pay dues by sharing great stories, laughing often, encouraging each other to live well and by contributing to a meaningful cause outside of golf. If interested, please make a request for membership on the clubs Flockbook page or send an email request to our Caddie Master at caddiemaster@brovenmail.com.
If you join through our Flockbook page, we encourage you to tag our page with testimonies about your common thread inspired experiences. For example, pictures of golf buddy trips and meaningful moments enjoying the great game with your family and friends.
We focus on what brings people together…
Target Market(s)
golfers who get the need to give back
Colors
Designer to choose colors to be used in the design.
Requirements
Must have
- clear messaging about the simple purpose vof the virtual club
- we can make up head quarter locations. like 19th holes around the world, global fairways, etc
- we do need a link to the club caddiemaster@brovenmail.com
- logo very visible
Nice to have
- course pictures.... I can upload or send a few good ones
Should not have
- Pictures of virtual golf. I changed the summary

```html
<!DOCTYPE html>
<html lang="en">
<head>
<meta charset="utf-8">
<title>Silver Lantern Golf Club – Cover</title>
<link href="https://fonts.googleapis.com/css2?family=Tinos:ital,wght@0,400;0,700;1,700&display=swap" rel="stylesheet">
<style>
  :root {
    --stage: #ececec;
    --orange: #f7941d;
    --orange-deep: #e6850f;
    --green: #3e5409;
    --white: #ffffff;
    --ink: #111111;
    --band-shade: #d9d9d9;
    --photo-sky: #e9b27a;
    --photo-haze: #b9b59c;
    --photo-grass: #4d8a2a;
    --photo-grass-deep: #2f6a1c;
  }
  html, body {
    margin: 0;
    padding: 0;
    width: 1200px;
    height: 1200px;
    overflow: hidden;
    background: var(--stage);
    font-family: "Tinos", "Times New Roman", serif;
  }
  .cover {
    position: absolute;
    left: 0;
    top: 378px;
    width: 1200px;
    height: 444px;
    overflow: hidden;
  }
  .cover-art {
    position: absolute;
    inset: 0;
    display: block;
  }
  .club-mark {
    position: absolute;
    left: 160px;
    top: 72px;
    width: 300px;
    height: 300px;
    display: flex;
    align-items: center;
    justify-content: center;
    text-align: center;
    color: var(--white);
    font-size: 34px;
    font-weight: 700;
    line-height: 1.15;
    letter-spacing: 2px;
    text-transform: uppercase;
  }
  .intro {
    position: absolute;
    left: 688px;
    top: 12px;
    width: 500px;
  }
  .intro-title {
    margin: 0;
    font-size: 32px;
    font-weight: 400;
    color: var(--ink);
    line-height: 1.1;
    white-space: nowrap;
  }
  .intro-text {
    margin: 4px 0 0;
    font-size: 21px;
    line-height: 26px;
    color: var(--white);
  }
  .membership {
    position: absolute;
    left: 688px;
    top: 164px;
    width: 500px;
    font-size: 16px;
    line-height: 21px;
    color: var(--orange);
  }
  .membership p { margin: 0; }
  .membership strong { color: var(--ink); font-weight: 700; }
  .rules-title {
    margin: 10px 0 2px !important;
    color: var(--ink);
    font-size: 15px;
    text-transform: uppercase;
  }
  .rules-list {
    list-style: none;
    margin: 0;
    padding: 0;
    font-size: 14px;
    line-height: 18px;
  }
  .dues {
    position: absolute;
    left: 690px;
    top: 327px;
    width: 500px;
    color: var(--white);
  }
  .dues-title {
    margin: 0;
    font-size: 30px;
    font-weight: 400;
    color: var(--orange);
    line-height: 1.1;
  }
  .dues-text {
    margin: 2px 0 0;
    font-size: 14.5px;
    line-height: 18px;
  }
  .dues-text a {
    color: var(--orange);
    font-weight: 700;
    font-style: italic;
    text-decoration: none;
  }
</style>
</head>
<body>
<section class="cover">
  <svg class="cover-art" width="1200" height="444" viewBox="0 0 1200 444">
    <defs>
      <linearGradient id="course-tones" x1="0" y1="0" x2="0" y2="1">
        <stop offset="0" stop-color="var(--photo-sky)"/>
        <stop offset="0.35" stop-color="var(--photo-haze)"/>
        <stop offset="0.5" stop-color="var(--photo-grass)"/>
        <stop offset="1" stop-color="var(--photo-grass-deep)"/>
      </linearGradient>
      <clipPath id="inner-panel">
        <path d="M616 0 Q732 222 616 444 L1200 444 L1200 0 Z"/>
      </clipPath>
    </defs>
    <rect class="course-photo" x="0" y="0" width="700" height="444" fill="url(#course-tones)" role="img" aria-label="Golf course fairway at sunset with trees and misty countryside"/>
    <circle class="mark-disc" cx="310" cy="222" r="170" fill="var(--orange)" fill-opacity="0.72"/>
    <path class="panel-edge" d="M602 0 Q718 222 602 444 L1200 444 L1200 0 Z" fill="var(--orange)"/>
    <g clip-path="url(#inner-panel)">
      <rect class="membership-band" x="600" y="143" width="600" height="165" fill="var(--white)"/>
      <polygon class="band-shade" points="600,143 1200,143 1200,165 760,152 600,150" fill="var(--band-shade)"/>
      <rect class="dues-band" x="600" y="308" width="600" height="136" fill="var(--green)"/>
    </g>
  </svg>

  <div class="club-mark">Silver Lantern<br>Golf Club</div>

  <header class="intro">
    <h1 class="intro-title">SILVER LANTERN GOLF CLUB</h1>
    <p class="intro-text">Is a virtual golf club community dedicated to building productive relationships beginning with the unifying foundation of the great game.</p>
  </header>

  <div class="membership">
    <p>Membership in the <strong>Silver Lantern Golf Club</strong> is simple. ask to join. The Membership Committee accepts a prospective member request upon confirmation of support for the club’s purpose.</p>
    <p class="rules-title">The Silver Lantern Golf Club has only two rules:</p>
    <ul class="rules-list">
      <li>1.) Create productive relationships building around an initial common thread</li>
      <li>2.) When tempted to cut the last relationship thread, remember rule #1</li>
    </ul>
  </div>

  <div class="dues">
    <h2 class="dues-title">WHAT ARE THE DUES?</h2>
    <p class="dues-text">Members pay dues by sharing great stories, laughing often, encouraging each other to live well and by contributing to a meaningful cause outside of golf.<br>If interested, please make a request for membership on the clubs Flockbook page or send an email request to our Caddie Master at <a href="mailto:caddiemaster@brovenmail.com">caddiemaster@brovenmail.com.</a></p>
  </div>
</section>
</body>
</html>
```